Advertisement Sign Project

Hi there,

I have a commercial space available for short term lease.

I need an advertisement sign to go on the double black doors (under the current Ferlomi Quintavo sign).

The advertising sign should be about A3 in size and designed to attract pedestrians.

See site address at 172 Dorrington Street Richmond Victoria Australia:

https://maps.plotvista.example/view?q=172A+Dorrington+St,+Richmond+Victoria+3121&ll=-37.800000,144.900000&z=17

Target Market(s)

Pop-up store tenants: fashion, textiles, bedding, furniture, homewares and kitchenwares.

The photos are provided to give you (the graphic designer) an idea of the space available.

Industry/Entity Type

Advertising

Requirements
Must have
• Retail tenancy available for short term lease.

For all enquiries contact Howell - 0417362908 or email howell@dorringtonwalkarcade.example

Nice to have
• Something befitting the look and feel of the building.

I was thinking a textile pattern as background, or some kind of fashion design element to inspire a potential pop up shop tenant.

```html
<!DOCTYPE html>
<html lang="en">
<head>
<meta charset="utf-8">
<title>Commercial Space Available for Short Term Lease</title>
<link rel="stylesheet" href="https://fonts.googleapis.com/css2?family=Anton&family=Arimo:wght@700&display=swap">
<style>
  :root {
    --brick-light: #e3d3b4;
    --brick-mid: #d3be99;
    --brick-dark: #b9a07c;
    --mortar: rgba(120, 100, 80, 0.28);
    --headline-red: #ff0000;
    --outline-white: #ffffff;
    --contact-red: #e8100f;
    --address-navy: #2b2f80;
    --photo-top: #4a3b30;
    --photo-mid: #6b5a4c;
    --photo-floor: #8c8478;
  }
  html, body {
    margin: 0;
    padding: 0;
    width: 849px;
    height: 1200px;
    overflow: hidden;
    background: var(--brick-light);
  }
  .poster {
    position: relative;
    width: 849px;
    height: 1200px;
    overflow: hidden;
  }
  .poster__backdrop {
    position: absolute;
    inset: 0;
    background:
      repeating-linear-gradient(180deg, transparent 0 112px, var(--mortar) 112px 122px),
      repeating-linear-gradient(90deg, transparent 0 262px, rgba(120,100,80,0.16) 262px 272px),
      radial-gradient(ellipse at 20% 30%, rgba(255,255,255,0.22), transparent 55%),
      radial-gradient(ellipse at 85% 75%, rgba(150,120,90,0.25), transparent 60%),
      linear-gradient(160deg, var(--brick-light) 0%, var(--brick-mid) 45%, var(--brick-light) 70%, var(--brick-dark) 100%);
  }
  .headline {
    position: absolute;
    left: 0;
    top: 0;
    width: 849px;
    height: 520px;
  }
  .headline text {
    font-family: "Anton", "Impact", sans-serif;
    font-size: 150px;
    fill: var(--headline-red);
    stroke: var(--outline-white);
    stroke-width: 5px;
    paint-order: stroke fill;
    filter: drop-shadow(3px 4px 3px rgba(0,0,0,0.45));
  }
  .space-photo {
    position: absolute;
    left: 83px;
    top: 527px;
    width: 669px;
    height: 447px;
    border: 6px solid var(--outline-white);
    border-radius: 3px;
    background: linear-gradient(180deg, var(--photo-top) 0%, var(--photo-mid) 45%, var(--photo-floor) 60%, #6f675d 100%);
  }
  .footer-text {
    position: absolute;
    left: 0;
    top: 980px;
    width: 849px;
    height: 220px;
  }
  .footer-text text {
    font-family: "Arimo", "Arial", sans-serif;
    font-weight: 700;
    font-size: 25px;
  }
  .footer-text .contact { fill: var(--contact-red); }
  .footer-text .business { fill: var(--address-navy); }
</style>
</head>
<body>
<main class="poster">
  <div class="poster__backdrop" role="img" aria-label="Faded photograph of a weathered cream brick wall"></div>

  <svg class="headline" viewBox="0 0 849 520" role="img" aria-labelledby="headline-title">
    <title id="headline-title">Commercial Space Available for Short Term Lease</title>
    <text x="78" y="176" textLength="712" lengthAdjust="spacingAndGlyphs">Commercial Space</text>
    <text x="192" y="337" textLength="476" lengthAdjust="spacingAndGlyphs">Available for</text>
    <text x="106" y="497" textLength="650" lengthAdjust="spacingAndGlyphs">Short Term Lease</text>
  </svg>

  <div class="space-photo" role="img" aria-label="Photograph of the empty warehouse interior with brick walls, steel column, fluorescent lights and concrete floor"></div>

  <svg class="footer-text" viewBox="0 980 849 220" role="img" aria-labelledby="footer-title">
    <title id="footer-title">Contact and business details</title>
    <text class="contact" x="82" y="1018" textLength="671" lengthAdjust="spacingAndGlyphs">For all enquiries contact Howell - 0417362908</text>
    <text class="contact" x="74" y="1045" textLength="691" lengthAdjust="spacingAndGlyphs">or email howell@dorringtonwalkarcade.example</text>
    <text class="business" x="412" y="1110" text-anchor="middle" textLength="112" lengthAdjust="spacingAndGlyphs">Ferlomi</text>
    <text class="business" x="141" y="1136" textLength="539" lengthAdjust="spacingAndGlyphs">172 Dorrington St, Richmond VIC 3121</text>
    <text class="business" x="148" y="1162" textLength="517" lengthAdjust="spacingAndGlyphs">(03) 9517 4826 · quintavo.example</text>
  </svg>
</main>
</body>
</html>
```